Orva Business Card

we need a business card for flooring business called Orva Flooring, the design should be black and white. we have 2 locations

Linmore Showroom
527 Kellerman Road,
Linmore VIC 3164

Harwick Showroom
462 Bramwell Hwy,
Harwick VIC 3287

email : sales@orvaflooring.com.au
(03) 9471 2830

Please inform we sell , Laminate, Hybrid, Timber, carpet and commercial flooring

```html
<!DOCTYPE html>
<html lang="en">
<head>
<meta charset="utf-8">
<title>Orva Flooring Business Card</title>
<link href="https://fonts.googleapis.com/css2?family=Montserrat:wght@300;400;700&display=swap" rel="stylesheet">
<style>
  :root {
    --backdrop: #2b2e33;
    --card: #1a1a1b;
    --ink: #f2f2f2;
    --ink-soft: #cfcfcf;
    --rule: #9a9a9a;
  }
  * { box-sizing: border-box; margin: 0; padding: 0; }
  html, body { width: 1200px; height: 900px; overflow: hidden; }
  body {
    background: var(--backdrop);
    font-family: "Montserrat", sans-serif;
    color: var(--ink);
    position: relative;
  }
  .card {
    position: absolute;
    top: 140px;
    width: 350px;
    height: 612px;
    background: var(--card);
    border-radius: 26px;
    display: flex;
    flex-direction: column;
    align-items: center;
    text-align: center;
  }
  .card--front { left: 205px; padding-top: 64px; }
  .card--back { left: 645px; justify-content: flex-end; padding-bottom: 120px; }
  .wordmark {
    font-weight: 300;
    color: var(--ink);
    letter-spacing: 3px;
    text-transform: uppercase;
    line-height: 1.15;
    display: flex;
    align-items: center;
    gap: 12px;
  }
  .wordmark__dot { width: 12px; height: 12px; border-radius: 50%; background: var(--ink); flex: none; }
  .card--front .wordmark { font-size: 26px; }
  .card--back .wordmark { font-size: 34px; }
  .person { margin-top: 48px; }
  .person__name { font-weight: 700; font-size: 25px; letter-spacing: 1.5px; text-transform: uppercase; }
  .person__role { font-weight: 400; font-size: 12px; letter-spacing: 1.5px; text-transform: uppercase; margin-top: 4px; color: var(--ink-soft); }
  .divider { display: flex; align-items: center; gap: 8px; margin: 20px 0 12px; }
  .divider__line { width: 62px; height: 1px; background: var(--rule); }
  .icon { width: 20px; height: 20px; background: var(--ink); border-radius: 3px; display: flex; align-items: center; justify-content: center; }
  .icon svg { width: 14px; height: 14px; }
  .contact { font-size: 15px; font-weight: 400; line-height: 1.6; }
  .showroom { font-size: 15px; font-weight: 400; line-height: 1.45; }
  .showroom-rule { width: 150px; height: 1px; background: var(--rule); margin: 14px 0; }
  .tagline { margin-top: 34px; font-size: 14px; line-height: 1.6; color: var(--ink-soft); padding: 0 30px; }
</style>
</head>
<body>
  <section class="card card--front">
    <div class="wordmark"><span class="wordmark__dot"></span><span>Orva<br>Flooring</span></div>
    <div class="person">
      <p class="person__name">Marcus Hale</p>
      <p class="person__role">Managing Director</p>
    </div>
    <div class="divider">
      <span class="divider__line"></span>
      <span class="icon"><svg viewBox="0 0 24 24"><path fill="#1a1a1b" d="M6.6 10.8a15 15 0 0 0 6.6 6.6l2.2-2.2a1 1 0 0 1 1-.25 11.4 11.4 0 0 0 3.6.57 1 1 0 0 1 1 1V20a1 1 0 0 1-1 1A17 17 0 0 1 3 4a1 1 0 0 1 1-1h3.5a1 1 0 0 1 1 1c0 1.25.2 2.45.57 3.6a1 1 0 0 1-.25 1z"/></svg></span>
      <span class="icon"><svg viewBox="0 0 24 24"><path fill="none" stroke="#1a1a1b" stroke-width="2" d="M3 6h18v12H3zM3 6l9 7 9-7"/></svg></span>
      <span class="divider__line"></span>
    </div>
    <p class="contact">(03) 9471 2830<br>sales@orvaflooring.com.au</p>
    <div class="divider">
      <span class="divider__line"></span>
      <span class="icon"><svg viewBox="0 0 24 24"><path fill="#1a1a1b" d="M12 2a7 7 0 0 0-7 7c0 5 7 13 7 13s7-8 7-13a7 7 0 0 0-7-7zm0 9.5A2.5 2.5 0 1 1 12 6.5a2.5 2.5 0 0 1 0 5z"/></svg></span>
      <span class="divider__line"></span>
    </div>
    <p class="showroom">Harwick Showroom<br>462 Bramwell Hwy,<br>Harwick VIC 3287</p>
    <span class="showroom-rule"></span>
    <p class="showroom">Linmore Showroom<br>527 Kellerman Road,<br>Linmore VIC 3164</p>
  </section>

  <section class="card card--back">
    <div class="wordmark"><span class="wordmark__dot"></span><span>Orva<br>Flooring</span></div>
    <p class="tagline">we sell , Laminate, Hybrid, Timber,<br>carpet and commercial flooring</p>
  </section>
</body>
</html>
```